Where's my Gym Buddy? looking to do two promotions as listed in project description

looking for two designs.

1: selfie frame design!! (wording) Frost Grind Carnival, my Summer fitness has started, Tag a friend who should be joining me. T.C Tag your posts to @brightloopsydney to win points for the competition. (Snow graphic) in a selfie frame design. this needs to be the same design but across different departments as seen at the top of the photo's I've attached EG: #brightloopfitness #brightloopindoor #brightloopswim #brightloopwyong

2: Selfie Frame Design!! (Wording) Where's my gym buddy?, Tag a friend who should be at the gym, T.C.Tag your posts to @brightloopsydney to win points for the competition. Spot the Pilot Feel Selfie frame design

Target Market(s)

Gym Members

Industry/Entity Type

Gym

Colors

Designer to choose colors to be used in the design.

Requirements
Must have
• quirky and funky design, must include wording listed, must be a selfie frame design
Should not have
• whilst we are a big corporate gym, we pride ourselves on having really funky advertisements, so please no boring business corporate typical designs

```html
<!DOCTYPE html>
<html lang="en">
<head>
<meta charset="utf-8">
<title>Frost Grind Carnival – Selfie Frame</title>
<link href="https://fonts.googleapis.com/css2?family=Archivo+Black&family=Oswald:wght@700&family=Open+Sans:wght@400;600&display=swap" rel="stylesheet">
<style>
  :root {
    --sky-deep: #5fb6e3;
    --sky-mid: #8ccdee;
    --sky-pale: #dcf1fb;
    --navy: #123a5c;
    --festival-red: #e5194a;
    --ribbon-teal: #2a9f8f;
    --ribbon-light: #37b7a6;
    --ribbon-fold: #1d7b6e;
    --ink: #2b2b2b;
    --white: #ffffff;
  }
  html, body {
    margin: 0;
    padding: 0;
    width: 1020px;
    height: 1200px;
    overflow: hidden;
    background: #ffffff;
  }
  .selfie-frame {
    position: relative;
    width: 1020px;
    height: 1200px;
    overflow: hidden;
  }
  .snow-backdrop {
    position: absolute;
    inset: 0;
    background: linear-gradient(180deg, var(--sky-deep) 0%, var(--sky-mid) 40%, var(--sky-pale) 62%, var(--sky-mid) 80%, var(--sky-deep) 100%);
  }
  .department-tag {
    position: absolute;
    top: 22px;
    left: 0;
    width: 100%;
    margin: 0;
    text-align: center;
    font-family: "Oswald", sans-serif;
    font-weight: 700;
    font-size: 44px;
    line-height: 56px;
    color: var(--navy);
  }
  .department-rule {
    position: absolute;
    top: 82px;
    left: 105px;
    width: 825px;
    height: 1px;
    background: var(--navy);
    opacity: 0.6;
  }
  .event-title {
    position: absolute;
    top: 94px;
    left: 0;
    width: 100%;
    margin: 0;
    text-align: center;
    font-family: "Archivo Black", sans-serif;
    font-size: 54px;
    line-height: 70px;
    color: var(--festival-red);
    text-transform: uppercase;
  }
  .frame-art {
    position: absolute;
    inset: 0;
  }
  .ribbon-text {
    font-family: "Open Sans", sans-serif;
    font-weight: 600;
    font-size: 30px;
    fill: var(--white);
  }
  .tag-band {
    position: absolute;
    top: 1046px;
    left: 152px;
    width: 734px;
    height: 37px;
    background: var(--ribbon-light);
    text-align: center;
    font-family: "Open Sans", sans-serif;
    font-size: 20px;
    line-height: 37px;
    color: var(--ink);
  }
  .competition-line {
    position: absolute;
    top: 1088px;
    left: 0;
    width: 100%;
    margin: 0;
    text-align: center;
    font-family: "Oswald", sans-serif;
    font-weight: 700;
    font-size: 34px;
    line-height: 46px;
    color: var(--ink);
  }
  .social-row {
    position: absolute;
    top: 1138px;
    left: 0;
    width: 100%;
    display: flex;
    justify-content: center;
    align-items: center;
    gap: 28px;
    font-family: "Open Sans", sans-serif;
    font-size: 25px;
    color: var(--ink);
  }
  .social-handle {
    display: flex;
    align-items: center;
    gap: 12px;
  }
  .social-handle::before {
    content: "";
    width: 22px;
    height: 22px;
    background: var(--navy);
  }
  .social-divider {
    width: 1px;
    height: 46px;
    background: var(--ink);
  }
</style>
</head>
<body>
  <main class="selfie-frame">
    <div class="snow-backdrop" role="img" aria-label="Icy blue winter backdrop with falling snow and snowflakes"></div>

    <h2 class="department-tag">#brightloopfitness</h2>
    <div class="department-rule"></div>
    <h1 class="event-title">Frost Grind Carnival</h1>

    <svg class="frame-art" width="1020" height="1200" viewBox="0 0 1020 1200" aria-hidden="true">
      <rect class="photo-border" x="152" y="364" width="734" height="674" fill="var(--festival-red)"/>
      <path class="photo-window" d="M184,330 Q522,240 860,330 L860,968 L184,968 Z" fill="var(--white)"/>

      <polygon class="ribbon-tail-left" points="48,296 236,246 236,326 200,360" fill="var(--ribbon-teal)"/>
      <polygon class="ribbon-fold-left" points="214,290 236,290 236,326" fill="var(--ribbon-fold)"/>
      <polygon class="ribbon-tail-right" points="990,306 802,246 802,326 860,374" fill="var(--ribbon-teal)"/>
      <polygon class="ribbon-fold-right" points="824,290 802,290 802,326" fill="var(--ribbon-fold)"/>

      <path class="ribbon-banner" d="M214,224 Q519,130 824,224 L824,290 Q519,200 214,290 Z" fill="var(--ribbon-light)"/>
      <path id="ribbon-curve" d="M224,270 Q519,172 814,270" fill="none"/>
      <text class="ribbon-text" text-anchor="middle">
        <textPath href="#ribbon-curve" startOffset="50%">My summer fitness has started</textPath>
      </text>
    </svg>

    <div class="tag-band">Tag a friend who should be joining me</div>
    <p class="competition-line">Post to our to win points for the competition</p>

    <div class="social-row">
      <span class="social-handle">@brightloopsydney</span>
      <span class="social-divider"></span>
      <span class="social-handle">@brightloopsydney</span>
    </div>
  </main>
</body>
</html>
```